Card Design to Advertise New Business

I am looking to have a card designed so that I can pass it out to help promote my business. I have never done this before so I honestly do not know where to start with any ideas. I am providing my website address to help. I provide math tutoring, test prep, and schooling options.

I am looking for a card bigger than a business card but smaller than a flyer. Something front and back that I can pass out.

Business Information
Phone: 470-526-1984
Website: www.brightmaplestudyhub.com
Address: 418 Larkwood Rd Ste 210 Marietta GA 30068
Email: brightmapleservices@kestrelpostmail.com

Services:
Math Tutoring
SAT & ACT Test Prep
Group and Private Sessions
Fully Accredited Private School

Target Market(s)

Middle and High School Students

Industry/Entity Type

Education

Requirements
Must have
• Information from my website

```html
<!DOCTYPE html>
<html lang="en">
<head>
<meta charset="utf-8">
<title>Bright Maple Study Hub – Promo Card</title>
<link href="https://fonts.googleapis.com/css2?family=Merriweather:wght@700&display=swap" rel="stylesheet">
<style>
  :root {
    --backdrop: #dfe9f4;
    --paper: #ffffff;
    --green: #00cc00;
    --brand-blue: #3a66cf;
    --ink: #111111;
    --star: #d8321c;
  }
  * { margin: 0; padding: 0; box-sizing: border-box; }
  html, body { width: 1200px; height: 811px; overflow: hidden; }
  body {
    background: var(--backdrop);
    font-family: "Merriweather", Georgia, serif;
    font-weight: 700;
    color: var(--ink);
    position: relative;
  }
  .card {
    position: absolute;
    top: 78px;
    width: 430px;
    height: 644px;
    background: var(--paper);
    overflow: hidden;
  }
  .card--front { left: 116px; }
  .card--back { left: 654px; }
  .card__shapes { position: absolute; inset: 0; }

  .front-brand {
    position: absolute;
    left: 55px;
    top: 235px;
    display: flex;
    align-items: center;
    gap: 14px;
  }
  .brand-mark {
    border-radius: 50%;
    background: var(--green);
    flex: none;
  }
  .front-brand .brand-mark { width: 116px; height: 116px; }
  .front-brand .brand-name {
    color: var(--brand-blue);
    font-size: 27px;
    line-height: 1.15;
  }

  .back-brand {
    position: absolute;
    left: 0; right: 0;
    top: 43px;
    text-align: center;
  }
  .back-brand .brand-mark {
    width: 52px; height: 52px;
    margin: 0 auto 6px;
  }
  .back-brand .brand-name {
    color: var(--brand-blue);
    font-size: 12px;
  }

  .contact {
    position: absolute;
    left: 0; right: 0;
    top: 155px;
    text-align: center;
    font-size: 10.6px;
    line-height: 16px;
  }
  .services {
    position: absolute;
    left: 0; right: 0;
    top: 271px;
    text-align: center;
    list-style: none;
    font-size: 15px;
  }
  .services li { line-height: 20px; }
  .services .star {
    color: var(--star);
    font-size: 11px;
    line-height: 12px;
  }
  .website {
    position: absolute;
    left: 0; right: 0;
    top: 463px;
    text-align: center;
    font-size: 10.6px;
  }
</style>
</head>
<body>
  <section class="card card--front">
    <svg class="card__shapes" width="430" height="644" viewBox="0 0 430 644" aria-hidden="true">
      <circle cx="-30" cy="-60" r="182" fill="var(--green)"/>
      <circle cx="149" cy="128" r="20.5" fill="var(--green)"/>
      <circle cx="238" cy="377" r="5.7" fill="var(--green)"/>
      <circle cx="244" cy="464" r="12" fill="var(--green)"/>
      <circle cx="450" cy="700" r="224" fill="var(--green)"/>
    </svg>
    <div class="front-brand">
      <span class="brand-mark"></span>
      <p class="brand-name">Bright Maple<br>Study Hub</p>
    </div>
  </section>

  <section class="card card--back">
    <svg class="card__shapes" width="430" height="644" viewBox="0 0 430 644" aria-hidden="true">
      <circle cx="-30" cy="-60" r="166" fill="var(--green)"/>
      <circle cx="470" cy="660" r="167" fill="var(--green)"/>
    </svg>
    <div class="back-brand">
      <div class="brand-mark"></div>
      <p class="brand-name">Bright Maple Study Hub</p>
    </div>
    <div class="contact">
      <p>Phone: 470-526-1984</p>
      <p>Address: 418 Larkwood Rd Ste 210 Marietta GA 30068</p>
      <p>Email: brightmapleservices@kestrelpostmail.com</p>
    </div>
    <ul class="services">
      <li>Math Tutoring</li>
      <li class="star">★</li>
      <li>SAT &amp; ACT Test Prep</li>
      <li class="star">★</li>
      <li>Group and Private Sessions</li>
      <li class="star">★</li>
      <li>Fully Accredited Private School</li>
    </ul>
    <p class="website">www.brightmaplestudyhub.com</p>
  </section>
</body>
</html>
```